Harbor Lantern Vodka needs new design for its Chili Vodka line

use the existing label attached to add a chili aspect to the label for our new Chili Vodka.

Target Market(s)

high end

Requirements
Must have
• creative image
Nice to have
• red chili peppers
Should not have
• fire

```html
<!DOCTYPE html>
<html lang="en">
<head>
<meta charset="UTF-8">
<title>Harbor Lantern Vodka – Chili Label</title>
<link rel="stylesheet" href="https://fonts.googleapis.com/css2?family=Montserrat:wght@500;600;700&family=Roboto:wght@400;500;700&display=swap">
<style>
  :root {
    --backdrop: #ffffff;
    --label-paper: #f3f3f1;
    --label-edge: #e2e2df;
    --gold: #c8962f;
    --gold-frame: #d2a23c;
    --ink: #262626;
    --chili-red: #a3231f;
    --chili-dark: #6e1512;
  }
  * { margin: 0; padding: 0; box-sizing: border-box; }
  html, body {
    width: 1200px;
    height: 1200px;
    overflow: hidden;
    background: var(--backdrop);
  }
  .label {
    position: absolute;
    left: 217px;
    top: 80px;
    width: 765px;
    height: 1040px;
    background: var(--label-paper);
    border: 1px solid var(--label-edge);
    font-family: "Roboto", Arial, sans-serif;
    color: var(--ink);
  }
  .label__frame {
    position: absolute;
    inset: 34px;
    border: 3px solid var(--gold-frame);
  }
  .label__distillery {
    position: absolute;
    top: 88px;
    left: 0;
    width: 100%;
    text-align: center;
    font-size: 19px;
    font-weight: 500;
    letter-spacing: 1px;
  }
  .label__wordmark {
    position: absolute;
    top: 250px;
    left: 0;
    width: 100%;
    text-align: center;
    font-family: "Montserrat", Arial, sans-serif;
    font-weight: 600;
    color: var(--gold);
    line-height: 1;
  }
  .label__wordmark-line { display: block; }
  .label__wordmark-line--harbor { font-size: 76px; letter-spacing: 4px; }
  .label__wordmark-line--lantern { font-size: 92px; letter-spacing: 2px; margin-top: 14px; }
  .label__wordmark-line--vodka { font-size: 84px; letter-spacing: 8px; margin-top: 14px; }
  .label__tagline {
    position: absolute;
    top: 688px;
    left: 0;
    width: 100%;
    text-align: center;
    font-size: 19px;
    font-weight: 500;
    letter-spacing: 2px;
  }
  .label__chili {
    position: absolute;
    left: 150px;
    top: 770px;
    width: 424px;
    height: 180px;
    border-radius: 90px;
    background: radial-gradient(ellipse at 45% 50%, var(--chili-red) 0%, var(--chili-dark) 100%);
  }
  .label__abv {
    position: absolute;
    left: 58px;
    top: 908px;
    font-size: 21px;
    font-weight: 700;
    line-height: 1.05;
  }
  .label__abv-unit {
    display: block;
    font-size: 15px;
    font-weight: 400;
  }
  .label__volume {
    position: absolute;
    left: 560px;
    top: 918px;
    font-size: 27px;
    font-weight: 700;
  }
</style>
</head>
<body>
  <main class="label">
    <div class="label__frame"></div>
    <p class="label__distillery">GREY FJORD DISTILLERY</p>
    <h1 class="label__wordmark">
      <span class="label__wordmark-line label__wordmark-line--harbor">HARBOR</span>
      <span class="label__wordmark-line label__wordmark-line--lantern">LANTERN</span>
      <span class="label__wordmark-line label__wordmark-line--vodka">VODKA</span>
    </h1>
    <p class="label__tagline">PREMIUM QUALITY</p>
    <div class="label__chili" role="img" aria-label="Engraved illustration of two red chili peppers"></div>
    <p class="label__abv">40%<span class="label__abv-unit">Alc/Vol</span></p>
    <p class="label__volume">70cl</p>
  </main>
</body>
</html>
```